Plakat-Design für Immobilienmakler und Baufinanzierer
Zielgruppe
Wir sind Immobilienmakler und Baufinanzierer und suchen ein hochwertiges Design, unsere Zielgruppe sind Kunden, die Ihr Haus verkaufen möchten. Für jeden erfolgreichen Verkauf spenden wir 5 % unserer Maklercourtage an einen Verein, den sich der Kunde aussuchen darf. Mit diesem Plakat wollen wir auf unsere Vereinsförderng aufmerksam machen und Vereine ansprechen.
Aufgabenstellung
Text: 'Wir spenden 5 % unserer Provision für Ihren Verein', 'Nur 1,99 % Maklercourtage', Logo, Kontaktdaten

```html
<!DOCTYPE html>
<html lang="de">
<head>
<meta charset="utf-8">
<title>Altmann Immobilien – Vereinsförderung</title>
<link href="https://fonts.googleapis.com/css2?family=Raleway:wght@400;500;700;800&display=swap" rel="stylesheet">
<style>
  :root {
    --teal: #005a70;
    --teal-soft: #3f6f82;
    --grey: #9b9b9b;
    --grey-line: #a9a9a9;
    --ink-soft: #6d6d6d;
    --white: #ffffff;
  }
  * { margin: 0; padding: 0; box-sizing: border-box; }
  html, body { width: 848px; height: 1200px; overflow: hidden; background: var(--white); }
  .poster {
    position: relative;
    width: 848px;
    height: 1200px;
    overflow: hidden;
    font-family: "Raleway", sans-serif;
    background: var(--white);
  }
  .brand {
    position: absolute;
    top: 98px;
    left: 0;
    width: 848px;
    text-align: center;
  }
  .brand-name {
    font-weight: 500;
    font-size: 27px;
    letter-spacing: 2px;
    color: var(--teal-soft);
  }
  .brand-rule {
    width: 338px;
    height: 1px;
    margin: 10px auto 0;
    background: var(--grey-line);
  }
  .brand-tagline {
    margin-top: 7px;
    font-size: 8px;
    letter-spacing: 5.2px;
    color: var(--ink-soft);
  }
  .headline {
    position: absolute;
    top: 204px;
    left: 0;
    width: 848px;
    text-align: center;
    font-weight: 800;
    font-size: 42.5px;
    letter-spacing: 1.2px;
    color: var(--teal);
  }
  .band-top {
    position: absolute;
    top: 294px;
    left: 0;
    width: 848px;
    height: 227px;
    background: var(--teal);
  }
  .band-top-accent {
    position: absolute;
    top: 400px;
    right: 0;
    width: 190px;
    height: 121px;
    background: var(--grey);
  }
  .band-top-stripe {
    position: absolute;
    top: 294px;
    left: 576px;
    width: 8px;
    height: 227px;
    background: var(--white);
  }
  .donation {
    position: absolute;
    top: 330px;
    left: 44px;
    color: var(--white);
    font-weight: 700;
    text-transform: uppercase;
  }
  .donation-lead { font-size: 43px; letter-spacing: 1.5px; line-height: 52px; font-weight: 800; }
  .donation-line { font-size: 31px; letter-spacing: 1.3px; line-height: 44px; }
  .photo {
    position: absolute;
    top: 521px;
    left: 0;
    width: 848px;
    height: 402px;
    background: linear-gradient(180deg, #e9e9e9 0%, #d2d2d2 22%, #6e6e6e 45%, #5a5a5a 70%, #8a8a8a 100%);
  }
  .band-bottom {
    position: absolute;
    top: 923px;
    left: 0;
    width: 848px;
    height: 138px;
    background: var(--grey);
  }
  .band-bottom-accent {
    position: absolute;
    top: 963px;
    left: 0;
    width: 185px;
    height: 98px;
    background: var(--teal);
  }
  .band-bottom-stripe {
    position: absolute;
    top: 923px;
    left: 185px;
    width: 8px;
    height: 138px;
    background: var(--white);
  }
  .fee {
    position: absolute;
    top: 948px;
    right: 43px;
    text-align: right;
    color: var(--white);
    font-weight: 700;
    text-transform: uppercase;
  }
  .fee-amount { font-size: 34px; letter-spacing: 1.4px; line-height: 44px; }
  .fee-label { font-size: 35px; letter-spacing: 1.4px; line-height: 44px; }
  .contact {
    position: absolute;
    top: 1132px;
    font-size: 22px;
    color: var(--teal-soft);
    font-weight: 400;
  }
  .contact-phone { left: 117px; }
  .contact-email { left: 437px; }
</style>
</head>
<body>
<main class="poster">
  <header class="brand">
    <div class="brand-name">ALTMANN IMMOBILIEN</div>
    <div class="brand-rule"></div>
    <div class="brand-tagline">IMMOBILIEN &amp; BAUFINANZIERUNG</div>
  </header>

  <h1 class="headline">WIR VERKAUFEN IHRE IMMOBILIE</h1>

  <div class="band-top" aria-hidden="true"></div>
  <div class="band-top-accent" aria-hidden="true"></div>
  <div class="band-top-stripe" aria-hidden="true"></div>

  <section class="donation">
    <div class="donation-lead">Wir spenden 5 %</div>
    <div class="donation-line">Unserer Provision</div>
    <div class="donation-line">Für Ihren Verein</div>
  </section>

  <div class="photo" role="img" aria-label="Fußballmannschaft kniet im Kreis auf dem Rasen bei einer Teambesprechung, Schwarzweißfoto"></div>

  <div class="band-bottom" aria-hidden="true"></div>
  <div class="band-bottom-accent" aria-hidden="true"></div>
  <div class="band-bottom-stripe" aria-hidden="true"></div>

  <section class="fee">
    <div class="fee-amount">Nur 1,99 %</div>
    <div class="fee-label">Maklercourtage</div>
  </section>

  <div class="contact contact-phone">+49 160 482 715 03</div>
  <div class="contact contact-email">info@immobilien-altmann.de</div>
</main>
</body>
</html>
```